"Sketch Onward Loop" Social Art Website Design

I need a design for a website I am building, which will be called Sketch Onward Loop. I have attached the selected logo for the site. The site will be about drawing/art, and how art can be used to brighten a stranger's day as a random act of kindness. In real life, people will receive a drawing or piece of art with details for this site on it. They will in turn be able to give a drawing or piece of art to someone else, thus building a 'chain' of people who are related to each other through the drawings they have received. This should create a strong 'social' aspect to the site. There will be areas of the site for seeing other drawings/art that have been submitted, as well as for seeing different statistics (how many drawings have been submitted, where, how people are connected, etc.).

Target Market(s)

No specific target market.

Industry/Entity Type

Building

Coding

Coded - Design and coding required

Number of Pages Required

1 page

Font styles to use
Sans Serif
Decorative

Requirements
Must have
• Must use the logo supplied.
Nice to have
• Should be colourful and artistic. References to art tools should be primarily around drawing, though painting can also feature. Colour scheme to match the logo would be ideal.

```html
<!DOCTYPE html>
<html lang="en">
<head>
<meta charset="utf-8">
<title>Sketch Onward Loop</title>
<link rel="stylesheet" href="https://fonts.googleapis.com/css2?family=Open+Sans:wght@400;600;700&family=Roboto+Condensed:wght@400&display=swap">
<style>
  :root {
    --pink: #ee3e80;
    --teal: #3ab4c8;
    --orange: #fbb040;
    --green: #8dc63f;
    --ink: #222222;
    --text: #555555;
    --muted: #9a9a9a;
    --line: #dcdcdc;
    --band: #eeeff1;
    --white: #ffffff;
  }
  * { box-sizing: border-box; margin: 0; padding: 0; }
  html, body { width: 1024px; height: 1200px; overflow: hidden; }
  body {
    position: relative;
    background: var(--white);
    font-family: "Open Sans", Arial, sans-serif;
    color: var(--text);
  }
  .abs { position: absolute; }

  /* Header */
  .site-header { position: absolute; left: 0; top: 0; width: 1024px; height: 50px; background: var(--white); border-bottom: 1px solid #ececec; z-index: 5; }
  .brand { position: absolute; left: 74px; top: 15px; display: flex; align-items: center; gap: 6px; font-size: 12px; font-weight: 600; color: var(--ink); }
  .brand-dot { width: 12px; height: 12px; border-radius: 50%; background: var(--pink); }
  .main-nav { position: absolute; left: 442px; top: 19px; width: 430px; display: flex; justify-content: space-between; font-size: 9.5px; font-weight: 700; color: var(--ink); white-space: nowrap; }
  .sign-in { position: absolute; left: 886px; top: 13px; width: 61px; height: 24px; background: var(--pink); border: 2px solid var(--ink); color: var(--white); font-size: 10px; font-weight: 700; display: flex; align-items: center; justify-content: center; box-shadow: 2px 2px 0 var(--pink); }

  /* Hero */
  .hero-bg { position: absolute; left: 0; top: 50px; width: 1024px; height: 662px; }
  .social-list { position: absolute; left: 971px; top: 134px; display: flex; flex-direction: column; gap: 11px; }
  .social-dot { width: 26px; height: 26px; border-radius: 50%; }

  .welcome { position: absolute; left: 601px; top: 140px; font-family: "Roboto Condensed", sans-serif; color: var(--pink); font-size: 26px; line-height: 1; }
  .hero-title { position: absolute; left: 600px; top: 166px; font-family: "Roboto Condensed", sans-serif; font-weight: 400; color: var(--teal); font-size: 33px; line-height: 1; white-space: nowrap; }
  .hero-copy { position: absolute; left: 602px; top: 210px; width: 345px; font-size: 10px; line-height: 19px; }

  .btn { position: absolute; height: 30px; border: 2px solid var(--ink); font-size: 10px; font-weight: 700; color: var(--ink); display: flex; align-items: center; justify-content: center; }
  .btn-orange { background: var(--orange); box-shadow: 3px 3px 0 var(--orange); }
  .btn-teal { background: var(--teal); box-shadow: 3px 3px 0 var(--teal); }
  .btn-green { background: var(--green); box-shadow: 3px 3px 0 var(--green); }

  .section-title { font-family: "Roboto Condensed", sans-serif; font-weight: 400; color: var(--pink); font-size: 25px; line-height: 1; white-space: nowrap; }
  .believe-title { position: absolute; right: 451px; top: 492px; }
  .believe-copy { position: absolute; left: 110px; top: 522px; width: 463px; text-align: right; font-size: 10.5px; line-height: 21px; }

  /* Gallery */
  .gallery { position: absolute; left: 0; top: 712px; width: 1024px; height: 246px; background: linear-gradient(#e9eaec, #f6f6f7 60%, #eeeff1); }
  .gallery-title { position: absolute; left: 0; width: 1024px; top: 16px; text-align: center; }
  .gallery-item { position: absolute; top: 51px; height: 156px; }
  .gallery-item.is-active { border: 2px solid var(--pink); box-shadow: -2px 2px 0 var(--ink); }
  .zoom { position: absolute; left: 50%; top: 50%; width: 30px; height: 30px; margin: -17px 0 0 -17px; border-radius: 50%; background: var(--pink); display: flex; align-items: center; justify-content: center; }

  /* Contact */
  .contact-title { position: absolute; left: 130px; top: 980px; font-size: 23px; }
  .contact-item { position: absolute; left: 135px; display: flex; gap: 10px; font-size: 10px; line-height: 15px; color: var(--text); }
  .contact-icon { flex: none; width: 23px; height: 23px; border-radius: 50%; background: var(--pink); display: flex; align-items: center; justify-content: center; }
  .field { position: absolute; border: 1px solid var(--line); background: var(--white); font-size: 10px; color: var(--muted); display: flex; align-items: center; gap: 6px; padding-left: 10px; }
  .field.message { align-items: flex-start; padding-top: 9px; }

  /* Footer */
  .site-footer { position: absolute; left: 0; top: 1158px; width: 1024px; height: 42px; background: var(--teal); }
  .copyright { position: absolute; left: 76px; top: 14px; font-size: 10px; color: var(--white); }
</style>
</head>
<body>

<header class="site-header">
  <div class="brand"><span class="brand-dot"></span>Sketch Onward Loop</div>
  <nav class="main-nav">
    <span>HOME</span><span>FIND A DRAWING</span><span>ABOUT</span><span>FAQ</span><span>CONTACT</span><span>REPORT</span><span>OUR POLICIES</span>
  </nav>
  <div class="sign-in">SIGN IN</div>
</header>

<svg class="hero-bg" viewBox="0 0 1024 662" aria-hidden="true">
  <defs>
    <radialGradient id="heroGlow" cx="0.6" cy="0.35" r="0.7">
      <stop offset="0" stop-color="#ffffff"/>
      <stop offset="1" stop-color="#e6e8eb"/>
    </radialGradient>
  </defs>
  <rect width="1024" height="662" fill="url(#heroGlow)"/>
  <polygon points="0,420 1024,320 1024,662 0,662" fill="#ffffff"/>
</svg>

<svg class="abs" style="left:0;top:60px" width="612" height="430" viewBox="0 0 612 430" role="img" aria-label="Illustration of a colourful hand holding a paintbrush sweeping out green leaves and red flowers">
  <defs>
    <linearGradient id="handArt" x1="0" y1="0" x2="1" y2="1">
      <stop offset="0" stop-color="#2aa6a0"/>
      <stop offset="0.45" stop-color="#e98a5c"/>
      <stop offset="1" stop-color="#4a8fd6"/>
    </linearGradient>
  </defs>
  <polygon points="0,20 180,10 430,120 610,300 400,430 300,430 0,300" fill="url(#handArt)" opacity="0.85"/>
</svg>

<div class="social-list" aria-label="Social links">
  <span class="social-dot" style="background:#5a78b8"></span>
  <span class="social-dot" style="background:#e24b4b"></span>
  <span class="social-dot" style="background:#4aa3d8"></span>
  <span class="social-dot" style="background:#d64545"></span>
</div>

<div class="welcome">WELCOME</div>
<h1 class="hero-title">SKETCH ONWARD LOOP</h1>
<p class="hero-copy">Sketch Onward Loop is a site about making art and giving it to strangers as a random act of kindness. Each drawing will also be an invitation to join the site, and create your own art to pass on to more strangers.</p>
<div class="btn btn-orange" style="left:603px;top:278px;width:80px">READ MORE</div>

<svg class="abs" style="left:586px;top:374px" width="372" height="292" viewBox="0 0 372 292" role="img" aria-label="Diamond collage of street art and artists at work">
  <polygon points="222,0 292,70 222,140 152,70" fill="#3e8fb5"/>
  <polygon points="145,77 212,144 145,211 78,144" fill="#a9b85a"/>
  <polygon points="299,77 369,147 299,217 229,147" fill="#5fa6c9"/>
  <polygon points="222,147 292,217 222,287 152,217" fill="#c53a7a"/>
  <polygon points="73,150 143,220 73,290 3,220" fill="#9a8570"/>
</svg>

<h2 class="section-title believe-title">WHAT WE BELIEVE</h2>
<p class="believe-copy">We believe that the gift of hand-made art – a simple drawing with a nice message for a stranger can brighten someone’s day and make the world just a little bit better. We also believe everyone is an artist, whether or not you’ve had any training or think you have any artistic talent. We created Sketch Onward Loop to join people together through art, creating an artistic chain of smiling people linked together through the simple act of drawing.</p>
<div class="btn btn-teal" style="left:490px;top:650px;width:80px">READ MORE</div>

<section class="gallery">
  <h2 class="section-title gallery-title">OUR ART GALLERY</h2>
  <div class="gallery-item" role="img" aria-label="Vintage poster of a woman seated on a blue sofa" style="left:70px;width:211px;background:linear-gradient(135deg,#c9b58c,#5c78b0 55%,#8a4a3a)"></div>
  <div class="gallery-item is-active" role="img" aria-label="Pale watercolour of a swan" style="left:292px;width:220px;background:linear-gradient(135deg,#d7e4ec,#b8c9d6 60%,#c6d3c5)">
    <span class="zoom"><svg width="12" height="12" viewBox="0 0 12 12"><circle cx="5" cy="5" r="3.2" fill="none" stroke="#fff" stroke-width="1.6"/><line x1="7.4" y1="7.4" x2="10.5" y2="10.5" stroke="#fff" stroke-width="1.8"/></svg></span>
  </div>
  <div class="gallery-item" role="img" aria-label="Street artist chalking a pavement drawing" style="left:522px;width:207px;background:linear-gradient(#6e6e6e,#9c9c9c 55%,#b58a4e)"></div>
  <div class="gallery-item" role="img" aria-label="Colourful mural beside a man standing at a wall" style="left:737px;width:218px;background:linear-gradient(135deg,#1f5a8a,#5dbb4a 55%,#2a2a3a)"></div>
</section>

<h2 class="section-title contact-title">CONTACT INFORMATION</h2>
<div class="contact-item" style="top:1017px">
  <span class="contact-icon"><svg width="10" height="12" viewBox="0 0 10 12"><path d="M5 0a4 4 0 0 1 4 4c0 3-4 8-4 8S1 7 1 4a4 4 0 0 1 4-4z" fill="#fff"/><circle cx="5" cy="4" r="1.4" fill="#ee3e80"/></svg></span>
  <span>Some address line here, City name,<br>Country name.</span>
</div>
<div class="contact-item" style="top:1059px">
  <span class="contact-icon"><svg width="11" height="11" viewBox="0 0 11 11"><path d="M2 0.5l2 2.2-1 1.3a6 6 0 0 0 4 4l1.3-1 2.2 2-1.3 1.7C5 10.5 0.5 6 0.3 1.8z" fill="#fff"/></svg></span>
  <span style="padding-top:4px">Phone: (123) 456 7890</span>
</div>
<div class="contact-item" style="top:1097px">
  <span class="contact-icon"><svg width="11" height="8" viewBox="0 0 11 8"><rect width="11" height="8" rx="1" fill="#fff"/><path d="M0.5 0.8 5.5 4.5 10.5 0.8" fill="none" stroke="#ee3e80" stroke-width="1"/></svg></span>
  <span style="padding-top:4px">Email: info@domain.com</span>
</div>

<div class="field" style="left:392px;top:980px;width:163px;height:32px">
  <svg width="8" height="9" viewBox="0 0 8 9"><circle cx="4" cy="2.3" r="2" fill="#bbb"/><path d="M0 9a4 3.5 0 0 1 8 0z" fill="#bbb"/></svg>Name
</div>
<div class="field" style="left:559px;top:980px;width:163px;height:32px">
  <svg width="9" height="9" viewBox="0 0 11 11"><path d="M2 0.5l2 2.2-1 1.3a6 6 0 0 0 4 4l1.3-1 2.2 2-1.3 1.7C5 10.5 0.5 6 0.3 1.8z" fill="#bbb"/></svg>Telephone
</div>
<div class="field" style="left:726px;top:980px;width:163px;height:32px">
  <svg width="10" height="7" viewBox="0 0 11 8"><rect width="11" height="8" rx="1" fill="#bbb"/><path d="M0.5 0.8 5.5 4.5 10.5 0.8" fill="none" stroke="#fff" stroke-width="1"/></svg>Email
</div>
<div class="field message" style="left:392px;top:1024px;width:497px;height:71px">
  <svg width="11" height="9" viewBox="0 0 11 9"><rect x="0.5" y="0.5" width="10" height="6" rx="1" fill="none" stroke="#bbb"/><path d="M3 6.5v2l2-2" fill="#bbb"/></svg>Your Message...
</div>
<div class="btn btn-green" style="left:392px;top:1110px;width:80px">READ MORE</div>

<footer class="site-footer">
  <span class="copyright">© 2016 All Rights Reserved</span>
</footer>
<svg class="abs" style="left:868px;top:1134px" width="50" height="48" viewBox="0 0 50 48" aria-hidden="true">
  <polygon points="22,0 48,24 22,48 2,24" fill="#ffffff"/>
  <polyline points="20,22 24,18 28,22" fill="none" stroke="#3ab4c8" stroke-width="1.5"/>
</svg>

</body>
</html>
```